The Willowmere Practice (willowmere.example)

One page website (already purchased the theme) introducing the online clinic, with video, sections on the page our process, the technology, blog, the practitioner, contact, testimonials, find out more (see copy below) I am in the closing stages of having some collateral prepared I will load up the files that are in place so far so you get the feel for the brand and the current progress on the a brochure. The theme I have currently is loaded with demo data . this needs to be deleted and replaced. See here willowmere.example.
Updates

Target Market(s)

Female 30-50

Coding

Coded - Design and coding required

Number of Pages Required

1 page

Font styles to use
Serif
Sans Serif

Colors
33a6d7
3277b5

Requirements
Must have
• Consistent feel with existing A4 brochure, Trifold Brochure and business card,

Intro image & Outcome statement - Recharge Your Energy
Video & Free Access Offer
Why Energy
Our Process
About Korvath Technology
Getting Started
About Bram
Our Services
Testimonials
Contact
Blog

Nice to have
• Suggestions for images.

```html
<!DOCTYPE html>
<html lang="en">
<head>
<meta charset="utf-8">
<title>The Willowmere Practice</title>
<link href="https://fonts.googleapis.com/css2?family=Roboto+Slab:wght@300;400;500;700&display=swap" rel="stylesheet">
<style>
:root{
  --ink:#1c2a2e;
  --body:#3c4a4f;
  --muted:#6b7a7f;
  --deep:#0e3c45;
  --teal:#5cc2cc;
  --teal-strong:#1fa3b3;
  --teal-mid:#45b2c0;
  --teal-soft:#e4f7fa;
  --grey:#f2f2f2;
  --white:#ffffff;
}
*{box-sizing:border-box;margin:0;padding:0}
html,body{width:1200px;height:5007px;overflow:hidden}
body{font-family:"Roboto Slab",serif;color:var(--body);background:var(--white);font-size:12px;line-height:1.5;position:relative}
.section{position:absolute;left:0;width:1200px}
.btn{position:absolute;display:inline-flex;align-items:center;gap:7px;background:var(--teal);color:var(--white);border-radius:20px;font-size:12px;padding:0 18px;height:30px;white-space:nowrap}
.btn .dot{width:12px;height:12px;border:2px solid var(--white);border-radius:50%;border-right-color:transparent}
.title-center{position:absolute;left:0;width:1200px;text-align:center;font-size:22px;font-weight:700;color:var(--deep);display:flex;justify-content:center;align-items:center;gap:14px}
.title-center::before,.title-center::after{content:"";width:28px;height:2px;background:var(--deep)}
.title-left{position:absolute;font-size:22px;font-weight:700;color:var(--deep);display:flex;align-items:center;gap:14px;white-space:nowrap}
.title-left::after{content:"";width:44px;height:2px;background:var(--deep)}
.photo{position:absolute}
p.copy{font-size:11.5px;line-height:1.6;color:var(--body)}

/* header + hero */
.hero{top:0;height:566px;background:linear-gradient(120deg,#2b3134 0%,#53595b 45%,#3a3f41 70%,#1e2326 100%)}
.topbar{position:absolute;top:0;left:0;width:1200px;height:70px;background:rgba(14,60,69,.92)}
.brand{position:absolute;display:flex;align-items:center;gap:8px;color:var(--white);font-size:17px;font-weight:500;white-space:nowrap}
.brand .mark{width:24px;height:24px;border-radius:50%;background:var(--white)}
.nav{position:absolute;left:422px;top:26px;display:flex;gap:26px;font-size:11.5px;color:#d3e4e7;white-space:nowrap}
.nav .active{color:var(--white);border-bottom:1px solid var(--white)}
.phone-pill{position:absolute;left:1039px;top:20px;width:130px;height:28px;border-radius:16px;background:var(--teal);color:var(--deep);font-size:11px;display:flex;align-items:center;justify-content:center;gap:8px}
.hero h1{position:absolute;left:0;top:252px;width:1200px;text-align:center;color:var(--white);font-size:38px;font-weight:500}
.hero .sub{position:absolute;left:0;top:302px;width:1200px;text-align:center;color:#e6eef0;font-size:20px;font-weight:300}
.dots{position:absolute;display:flex;gap:10px;align-items:center}
.dots i{width:7px;height:7px;border-radius:50%;background:var(--teal)}
.dots i.on{width:10px;height:10px;background:none;border:2px solid var(--teal)}

/* signup */
.signup{top:566px;height:222px}
.signup .left{position:absolute;left:0;top:0;width:609px;height:222px;background:var(--teal-soft)}
.signup .right{position:absolute;left:609px;top:0;width:591px;height:222px;background:linear-gradient(100deg,#6f8487,#a7b3b0 50%,#7e8d8c)}
.signup .kicker{position:absolute;left:0;width:609px;text-align:center;top:56px;font-size:19px;color:var(--ink)}
.signup h2{position:absolute;left:0;width:609px;text-align:center;top:80px;font-size:31px;font-weight:700;color:var(--deep)}
.field{position:absolute;left:229px;top:136px;width:317px;height:36px;border:2px solid var(--deep);border-radius:20px;background:var(--white);display:flex;align-items:center;padding-left:18px;font-size:10.5px;color:#9aa6a9}
.field .submit{position:absolute;right:3px;top:3px;height:26px;width:96px;border-radius:14px;background:var(--teal);color:var(--deep);font-size:12px;display:flex;align-items:center;justify-content:center}
.play{position:absolute;left:884px;top:92px}

/* why energy */
.why{top:788px;height:512px}
.why .block{position:absolute;left:249px;top:126px;width:286px;height:315px;background:var(--deep)}
.why .photo{left:181px;top:62px;width:338px;height:364px;background:linear-gradient(150deg,#d9d2c8,#b4aea6 50%,#8e8a86)}
.why .text{position:absolute;left:609px;top:96px;width:380px}
.why .lead{font-size:14px;line-height:1.55;color:var(--ink);margin-top:22px}
.why .strong{font-size:12.5px;font-weight:700;color:var(--ink);margin-top:12px}

/* process */
.process{top:1300px;height:441px;background:var(--grey)}
.pcard{position:absolute;top:116px;width:195px;height:263px;color:var(--white);display:flex;flex-direction:column;justify-content:flex-end;align-items:center;padding-bottom:12px;font-weight:700;font-size:14px}
.pcard .chev{width:8px;height:8px;border-right:2px solid var(--white);border-bottom:2px solid var(--white);transform:rotate(45deg);margin-top:4px}
.pcard.detect{left:181px;background:linear-gradient(160deg,#0b2a6a,#1f6fc0 55%,#0b2450)}
.pcard.correct{left:609px;background:linear-gradient(170deg,#d8d4d0,#b9b2ac 60%,#6a5d56)}
.pcard.reconnect{left:823px;background:linear-gradient(180deg,#e8a676,#e3735a 55%,#9b3f3a)}
.pcard.direct{left:395px;background:var(--deep);justify-content:flex-start;padding:18px 14px;box-shadow:0 8px 18px rgba(0,0,0,.35);text-align:center}
.pcard.direct h3{font-size:14px;margin-bottom:10px}
.pcard.direct p{font-size:11px;font-weight:400;line-height:1.45;color:#e4eef0}

/* steps */
.steps{top:1741px;height:451px;background:#f4f4f4}
.step{position:absolute;width:195px}
.step svg{display:block;margin-bottom:8px}
.step h4{font-size:13px;font-weight:500;color:var(--ink)}
.step h4 span{color:var(--teal-strong);font-weight:400}
.step p{font-size:10.5px;line-height:1.5;color:var(--body);margin-top:3px}
.step.raised{background:var(--white);padding:16px 18px;box-shadow:0 4px 12px rgba(0,0,0,.12)}
.outline-btn{position:absolute;left:852px;top:326px;width:136px;height:38px;border:1.5px solid var(--teal);border-radius:20px;display:flex;align-items:center;justify-content:center;gap:8px;font-size:12px;color:var(--ink);background:var(--white)}
.outline-btn .dot{width:12px;height:12px;border:2px solid var(--deep);border-radius:50%;border-right-color:transparent}

/* about */
.about{top:2192px;height:531px}
.about .name{position:absolute;left:181px;top:104px;font-size:14px;color:var(--ink);white-space:nowrap}
.about .name b{font-weight:700}
.about .name span{color:var(--muted);font-weight:300}
.about .intro{position:absolute;left:181px;top:140px;width:520px}
.checks{position:absolute;left:199px;top:210px;list-style:none}
.checks li{display:flex;align-items:center;gap:9px;font-size:11px;color:var(--ink);height:24px}
.checks li i{width:12px;height:12px;border:1.5px solid var(--teal-strong);border-radius:50%;position:relative}
.checks li i::after{content:"";position:absolute;left:4px;top:1px;width:1.5px;height:7px;background:var(--teal-strong)}
.about .block{position:absolute;left:764px;top:105px;width:253px;height:263px;background:var(--deep)}
.about .photo{left:739px;top:60px;width:267px;height:294px;background:linear-gradient(160deg,#dfe4e4,#b9c2c2 55%,#8f9da2)}
.about .outro{position:absolute;left:181px;top:392px;width:836px}

/* services */
.services{top:2723px;height:681px;background:var(--grey)}
.table{position:absolute;left:181px;top:119px;width:836px;background:var(--white);box-shadow:0 4px 14px rgba(0,0,0,.1)}
.row{display:grid;grid-template-columns:266px repeat(4,1fr);height:30px;align-items:center;border-bottom:1px solid #ececec}
.row .label{text-align:right;padding-right:12px;font-size:10.5px;color:var(--ink);white-space:nowrap}
.row .cell{display:flex;justify-content:center}
.row.head{height:38px;border:none}
.row.head .cell{height:38px;align-items:center;color:var(--white);font-size:12.5px}
.row.head .c1{background:var(--teal)}
.row.head .c2{background:#3fa9b8}
.row.head .c3{background:#63b5c0}
.row.head .c4{background:#2f9aa9}
.row.band{background:var(--teal-strong);color:var(--white);font-size:12px;font-weight:700;border:none}
.row.band .label{text-align:left;padding-left:12px;color:var(--white)}
.row.band .label span{font-weight:400;color:#d8f1f4}

/* technology */
.tech{top:3404px;height:471px}
.tech .copy-wrap{position:absolute;left:181px;top:108px;width:836px}
.tech .copy-wrap p{margin-bottom:14px}

/* testimonials */
.testimonials{top:3875px;height:472px;background:var(--grey)}
.tcard{position:absolute;top:157px;width:241px;height:198px;background:var(--white);box-shadow:0 4px 12px rgba(0,0,0,.1);text-align:center;padding:50px 16px 0}
.tcard .avatar{position:absolute;left:76px;top:-50px;width:88px;height:88px;border-radius:50%;border:4px solid var(--teal);background:linear-gradient(160deg,#c8cfd1,#8b979b)}
.tcard h5{font-size:12.5px;font-weight:700;color:var(--ink)}
.tcard .q{font-size:26px;color:var(--teal);line-height:1;margin-top:6px;height:22px}
.tcard p{font-size:10.5px;color:var(--muted);line-height:1.45;margin-top:4px}

/* blogs */
.blogs{top:4347px;height:438px}
.bcard{position:absolute;top:119px;width:241px}
.bcard .img{height:144px;position:relative}
.bcard .date{position:absolute;left:4px;top:0;background:var(--teal);color:var(--deep);font-size:10px;padding:6px 8px;line-height:1.1}
.bcard .date b{display:block;font-size:16px}
.bcard .meta{font-size:9.5px;color:var(--muted);margin-top:12px;display:flex;align-items:center;gap:6px}
.bcard .meta i{width:11px;height:9px;border:1px solid var(--muted)}
.bcard .ttl{font-size:11px;color:var(--ink);margin-top:6px;line-height:1.5}
.bcard .btn{position:relative;margin-top:14px;height:24px;font-size:10px;padding:0 13px;color:var(--deep)}

/* footer */
.footer{top:4785px;height:194px;background:var(--deep);color:#c9dadd}
.footer h6{position:absolute;font-size:14px;font-weight:500;color:var(--teal);display:flex;align-items:center;gap:8px}
.footer h6::after{content:"";width:26px;height:1.5px;background:var(--teal)}
.footer .links{position:absolute;font-size:10.5px;line-height:19.5px}
.footer .tag{position:absolute;left:185px;top:90px;font-size:11px;width:220px;color:var(--teal);line-height:1.4}
.contact{position:absolute;left:823px;top:68px;font-size:10.5px;color:var(--teal)}
.contact div{display:flex;gap:10px;align-items:flex-start;margin-bottom:9px}
.copybar{position:absolute;left:0;top:4979px;width:1200px;height:28px;background:var(--teal);color:var(--deep);font-size:9.5px}
.copybar span{position:absolute;left:181px;top:7px}
.social{position:absolute;left:917px;top:5px;display:flex;gap:9px}
.social i{width:18px;height:18px;border-radius:50%;background:var(--deep)}
</style>
</head>
<body>
<svg width="0" height="0" style="position:absolute">
  <symbol id="tick" viewBox="0 0 16 16"><circle cx="8" cy="8" r="8" fill="#45b2c0"/><path d="M4.5 8.2l2.3 2.3 4.7-4.7" fill="none" stroke="#fff" stroke-width="1.8"/></symbol>
  <symbol id="tick-light" viewBox="0 0 16 16"><circle cx="8" cy="8" r="8" fill="#fff"/><path d="M4.5 8.2l2.3 2.3 4.7-4.7" fill="none" stroke="#1fa3b3" stroke-width="1.8"/></symbol>
</svg>

<!-- Hero -->
<section class="section hero">
  <div class="photo" role="img" aria-label="Personal trainer guiding a woman through a dumbbell workout in a gym" style="left:0;top:0;width:1200px;height:566px"></div>
  <div class="topbar"></div>
  <div class="brand" style="left:31px;top:22px"><span class="mark"></span>The Willowmere Practice</div>
  <nav class="nav"><span class="active">Home</span><span>Video</span><span>Why Energy</span><span>Our Process</span><span>About Bram</span><span>Our Services</span><span>Contact</span><span>Blog</span></nav>
  <div class="phone-pill"><svg width="12" height="12" viewBox="0 0 24 24"><path d="M6.6 10.8a15 15 0 006.6 6.6l2.2-2.2a1 1 0 011-.25 11.4 11.4 0 003.6.6 1 1 0 011 1V20a1 1 0 01-1 1A17 17 0 013 4a1 1 0 011-1h3.5a1 1 0 011 1 11.4 11.4 0 00.6 3.6 1 1 0 01-.25 1z" fill="#0e3c45"/></svg>0400 000 123</div>
  <h1>Restore your Energy</h1>
  <div class="sub">for exceptional health and longevity</div>
  <div class="btn" style="left:542px;top:353px;color:var(--deep)"><span class="dot" style="border-color:var(--deep);border-right-color:transparent"></span>Read More</div>
  <div class="dots" style="left:578px;top:529px"><i></i><i class="on"></i><i></i></div>
</section>

<!-- Sign up -->
<section class="section signup">
  <div class="left"></div>
  <div class="right" role="img" aria-label="Two women resting after a run, listening to music on a bench"></div>
  <div class="kicker">Sign Up for Free</div>
  <h2>Access Offer Now!</h2>
  <div class="field">Enter Your Email<span class="submit">Submit</span></div>
  <svg class="play" width="40" height="40" viewBox="0 0 40 40"><circle cx="20" cy="20" r="18" fill="none" stroke="#5cc2cc" stroke-width="2.5"/><path d="M16 12l12 8-12 8z" fill="#5cc2cc"/></svg>
</section>

<!-- Why Energy -->
<section class="section why">
  <div class="block"></div>
  <div class="photo" role="img" aria-label="Practitioner giving a treatment to a client lying on a massage table"></div>
  <div class="text">
    <div class="title-left" style="position:relative">Why Energy</div>
    <p class="lead">It seems like an obvious answer, after all, <b>"more energy please"</b> is top of the wish list for most of our clients.</p>
    <p class="strong">But you may not know how vital energy is to how you feel.</p>
    <p class="copy" style="margin-top:16px">At cellular level, mitochondria are responsible for the functioning every cell in every organ and every system of your body, every second of your existence. If mitochondrial operation is under stress, you will feel it.</p>
    <p class="copy" style="margin-top:12px">But true to the teachings of traditional Chineses Medicine, energy flows, it can get stuck, and of course certain types of energy can be a hinderance to optimal operations as well.</p>
  </div>
  <div class="btn" style="left:609px;top:387px"><span class="dot"></span>Read More</div>
</section>

<!-- Our Process -->
<section class="section process">
  <h2 class="title-center" style="top:50px">Our Process</h2>
  <div class="pcard detect" role="img" aria-label="Digital body scan of a glowing human figure">Detect<span class="chev"></span></div>
  <div class="pcard direct"><h3>Direct</h3><p>use our Infotonics. These provide corrective information to the body-field, leading it back to a more optimal state so it can correctly guide the body's functions. The BioVital Wellness System recommends the Infotonics most critical for the body's wellness based on its body-field assessment.</p></div>
  <div class="pcard correct" role="img" aria-label="Drops of a remedy being added to a glass of water">Correct<span class="chev"></span></div>
  <div class="pcard reconnect" role="img" aria-label="Woman meditating at sunset with arms raised">Re-Connect<span class="chev"></span></div>
</section>

<!-- Steps -->
<section class="section steps">
  <h2 class="title-center" style="top:46px">Steps to Getting Started</h2>
  <div class="step" style="left:181px;top:126px">
    <svg width="28" height="26" viewBox="0 0 28 26"><rect x="2" y="3" width="18" height="20" rx="2" fill="#5cc2cc"/><path d="M6 9h10M6 13h10M6 17h6" stroke="#fff" stroke-width="1.6"/><path d="M18 20l8-8" stroke="#5cc2cc" stroke-width="3"/></svg>
    <h4><span>01.</span> Register</h4>
    <p>Get your lifetime access to our platform and access many benefits free: willowmere.example/KVT</p>
  </div>
  <div class="step" style="left:395px;top:126px">
    <svg width="28" height="26" viewBox="0 0 28 26"><rect x="6" y="4" width="16" height="20" rx="2" fill="none" stroke="#5cc2cc" stroke-width="2"/><path d="M10 4V1h8v3M14 10v8M10 14h8" stroke="#5cc2cc" stroke-width="2"/></svg>
    <h4><span>02.</span> Scanner</h4>
    <p>Buy a scanner in the shop within your account at portal.willowmere.example (or beg or borrow from friend of family member!)</p>
  </div>
  <div class="step raised" style="left:609px;top:111px;height:151px">
    <svg width="24" height="24" viewBox="0 0 24 24"><path d="M12 3v12M6 10l6 6 6-6M4 21h16" fill="none" stroke="#5cc2cc" stroke-width="2"/></svg>
    <h4><span>03.</span> Download</h4>
    <p>Download the smart phone app VitalPath</p>
  </div>
  <div class="step" style="left:823px;top:126px">
    <svg width="28" height="26" viewBox="0 0 28 26"><path d="M3 8V3h5M20 3h5v5M25 18v5h-5M8 23H3v-5" fill="none" stroke="#5cc2cc" stroke-width="2"/><rect x="9" y="8" width="10" height="10" fill="none" stroke="#5cc2cc" stroke-width="2"/></svg>
    <h4><span>04.</span> Scan</h4>
    <p>pair your scanner, with the app and follow instructions on how to scan</p>
  </div>
  <div class="step" style="left:181px;top:296px">
    <svg width="26" height="20" viewBox="0 0 26 20"><path d="M1 10s5-8 12-8 12 8 12 8-5 8-12 8S1 10 1 10z" fill="#5cc2cc"/><circle cx="13" cy="10" r="4" fill="#fff"/></svg>
    <h4><span>05.</span> View</h4>
    <p>view your results on you phone or sign back online for better viewing experience</p>
  </div>
  <div class="step" style="left:395px;top:296px">
    <svg width="32" height="20" viewBox="0 0 32 20"><path d="M1 8l8-5 7 4 7-4 8 5-8 5-7-3-7 3z" fill="#5cc2cc"/></svg>
    <h4><span>06.</span> Self Direct</h4>
    <p>follow simple guidelines on how to improve your results, or buy a " Feel Good" infotonics or</p>
  </div>
  <div class="step" style="left:609px;top:296px">
    <svg width="24" height="24" viewBox="0 0 24 24"><circle cx="12" cy="12" r="9" fill="none" stroke="#5cc2cc" stroke-width="3"/><circle cx="12" cy="12" r="4" fill="none" stroke="#5cc2cc" stroke-width="2"/></svg>
    <h4><span>07.</span> Get Help</h4>
    <p>pair your scanner, with the app and follow instructions on how to scan</p>
  </div>
  <div class="outline-btn"><span class="dot"></span>Get Started</div>
</section>

<!-- About Bram -->
<section class="section about">
  <h2 class="title-left" style="left:181px;top:58px">About Bram</h2>
  <div class="name"><b>Bram R Halloway</b> <span>FDN-P HPC PFC PBC</span></div>
  <p class="copy intro">Bram is a multimodality alternative health provider with a focus in shedding light on what holds you back from being as healthy as you want. He is a pioneer in the alternative health care space, and has established the Willowmere Practice to help you to:</p>
  <ul class="checks">
    <li><i></i>understand why you feel the way you do</li>
    <li><i></i>do to the right things to change your energy</li>
    <li><i></i>be empowered to do it yourself, or be guided by a practitioner</li>
    <li><i></i>give you online flexibility where ever you are in the world</li>
    <li><i></i>bring the cutting edge diagnostic technology into your home</li>
    <li><i></i>enjoy lifetime access to the software, for FREE</li>
  </ul>
  <div class="block"></div>
  <div class="photo" role="img" aria-label="Portrait of the practitioner smiling in a bright office"></div>
  <p class="copy outro">It took Bram almost 3 decades of trial and error, and false hope, for him to arrive at the same conclusion that leading experts in the field of bioenergetics had been saying since the beginning: energy drives biochemistry, not the other way round.</p>
  <div class="btn" style="left:181px;top:450px"><span class="dot"></span>Read More</div>
</section>

<!-- Services -->
<section class="section services">
  <h2 class="title-center" style="top:50px">Our Services</h2>
  <div class="table">
    <div class="row head"><span></span><span class="cell c1">Free</span><span class="cell c2">Active</span><span class="cell c3">Strategy</span><span class="cell c4">Transform</span></div>
    <div class="row band"><span class="label">Personal Account</span></div>
    <div class="row"><span class="label">Bioenergetic Music</span><span class="cell"><svg width="16" height="16"><use href="#tick"/></svg></span><span class="cell"><svg width="16" height="16"><use href="#tick"/></svg></span><span class="cell"><svg width="16" height="16"><use href="#tick"/></svg></span><span class="cell"><svg width="16" height="16"><use href="#tick"/></svg></span></div>
    <div class="row"><span class="label">Turning Tide - The Film</span><span class="cell"><svg width="16" height="16"><use href="#tick"/></svg></span><span class="cell"><svg width="16" height="16"><use href="#tick"/></svg></span><span class="cell"><svg width="16" height="16"><use href="#tick"/></svg></span><span class="cell"><svg width="16" height="16"><use href="#tick"/></svg></span></div>
    <div class="row"><span class="label">Bioenergetic Receipes</span><span class="cell"><svg width="16" height="16"><use href="#tick"/></svg></span><span class="cell"><svg width="16" height="16"><use href="#tick"/></svg></span><span class="cell"><svg width="16" height="16"><use href="#tick"/></svg></span><span class="cell"><svg width="16" height="16"><use href="#tick"/></svg></span></div>
    <div class="row"><span class="label">Bioenergetic Exercises</span><span class="cell"><svg width="16" height="16"><use href="#tick"/></svg></span><span class="cell"><svg width="16" height="16"><use href="#tick"/></svg></span><span class="cell"><svg width="16" height="16"><use href="#tick"/></svg></span><span class="cell"><svg width="16" height="16"><use href="#tick"/></svg></span></div>
    <div class="row"><span class="label">VitalPath Life Book</span><span class="cell"><svg width="16" height="16"><use href="#tick"/></svg></span><span class="cell"><svg width="16" height="16"><use href="#tick"/></svg></span><span class="cell"><svg width="16" height="16"><use href="#tick"/></svg></span><span class="cell"><svg width="16" height="16"><use href="#tick"/></svg></span></div>
    <div class="row band"><span class="label">Bioenergetic Scans</span></div>
    <div class="row"><span class="label">Scanner Yes Yes Yes</span><span class="cell"></span><span class="cell"><svg width="16" height="16"><use href="#tick"/></svg></span><span class="cell"><svg width="16" height="16"><use href="#tick"/></svg></span><span class="cell"><svg width="16" height="16"><use href="#tick"/></svg></span></div>
    <div class="row"><span class="label">Unlimited Lifetime Body Scans</span><span class="cell"></span><span class="cell"><svg width="16" height="16"><use href="#tick"/></svg></span><span class="cell"><svg width="16" height="16"><use href="#tick"/></svg></span><span class="cell"><svg width="16" height="16"><use href="#tick"/></svg></span></div>
    <div class="row band"><span class="label">Consulting</span></div>
    <div class="row"><span class="label">Scan Interpretation Call</span><span class="cell"></span><span class="cell"><svg width="16" height="16"><use href="#tick"/></svg></span><span class="cell"><svg width="16" height="16"><use href="#tick"/></svg></span><span class="cell"><svg width="16" height="16"><use href="#tick"/></svg></span></div>
    <div class="row"><span class="label">Group Webinar Scan Trainings</span><span class="cell"></span><span class="cell"><svg width="16" height="16"><use href="#tick"/></svg></span><span class="cell"><svg width="16" height="16"><use href="#tick"/></svg></span><span class="cell"><svg width="16" height="16"><use href="#tick"/></svg></span></div>
    <div class="row"><span class="label">Full Intake &amp; Strategy &amp; 30 Day Program</span><span class="cell"></span><span class="cell"></span><span class="cell"><svg width="16" height="16"><use href="#tick"/></svg></span><span class="cell"><svg width="16" height="16"><use href="#tick"/></svg></span></div>
    <div class="row"><span class="label">1 * Coaching Call</span><span class="cell"></span><span class="cell"></span><span class="cell"><svg width="16" height="16"><use href="#tick"/></svg></span><span class="cell"><svg width="16" height="16"><use href="#tick"/></svg></span></div>
    <div class="row band"><span class="label">Bespoke 90 Day Coaching <span>(By Application)</span></span><span class="cell"></span><span class="cell"></span><span class="cell"><svg width="16" height="16"><use href="#tick-light"/></svg></span><span class="cell"><svg width="16" height="16"><use href="#tick-light"/></svg></span></div>
  </div>
</section>

<!-- Technology -->
<section class="section tech">
  <h2 class="title-left" style="left:181px;top:58px">About Korvath Technology</h2>
  <div class="copy-wrap">
    <p class="copy"><b>KVT Health is the leader in bioenergetics</b>: the study, detection, and correction of energy in living systems. They spent decades mapping out the energy and communication systems of the body. Collectively, these are called the human body-field, which acts as a control system for the body's physical activity.</p>
    <p class="copy">When this field is underpowered or distorted, it's unable to run the body in an optimal way and the body's cells and systems may begin to fail. Symptoms often begin with simply feeling tired, but they can continue into just about any known health problem. When we improve function of the body-field, and we combine this with good nutrition and lifestyle choices, the body's incredible healing system can take over and begin to heal the body to health.</p>
    <p class="copy">At the Willowmere Practice, we furnish you with their scanning technology to provide you with a holistic wellness report in just seconds, from the comfort of your home. While this isn't a medical assessment, the scan's bioenergetic matching process often shows a strong correlation to known health concerns. But more important, this approach looks for the underlying problem so we can address health concerns from their roots with their bioenergetic solutions.</p>
    <p class="copy">The KVT software directs you specifically to exercises, routines, affirmations, to improve your results. It will offer some guidance on the take energy drops to take, called Infotonics. Without a practitioner, you may purchase on of the 19 Feel Good Infotonics. Otherwise you will need to will need to see a practitioner for strategy and prescription.</p>
  </div>
  <div class="btn" style="left:181px;top:376px"><span class="dot"></span>Read More</div>
</section>

<!-- Testimonials -->
<section class="section testimonials">
  <h2 class="title-center" style="top:50px">Testimonials</h2>
  <div class="tcard" style="left:220px"><div class="avatar" role="img" aria-label="Client portrait"></div><h5>Dr Helen Marsh</h5><div class="q">"</div><p>KVT Health truly offers insights into the body, both mind and physical well-being, that the medical community cannot comprehend often, nor understand. It is truly a remarkable system</p></div>
  <div class="tcard" style="left:480px"><div class="avatar" role="img" aria-label="Client portrait"></div><h5>Dr. Owen Carlisle, MD</h5><div class="q">"</div><p>provides the signal for the body to heal itself. What's hard to understand is it really doesn't do anything except provide the signal. The body does everything else</p></div>
  <div class="tcard" style="left:739px"><div class="avatar" role="img" aria-label="Client portrait"></div><h5>Rosa Pembury</h5><div class="q">"</div><p>Thanks to KVT, my energy has skyrocketed and I am accomplishing more than I have in years</p></div>
  <div class="dots" style="left:576px;top:408px"><i style="background:var(--deep)"></i><i class="on"></i><i style="background:var(--deep)"></i></div>
</section>

<!-- Blogs -->
<section class="section blogs">
  <h2 class="title-center" style="top:56px">Our Blogs</h2>
  <div class="bcard" style="left:220px">
    <div class="img" role="img" aria-label="Runner's shoes on a trail at sunrise" style="background:linear-gradient(170deg,#e9b27a,#b87a55 60%,#5a4034)"><div class="date">22/09<b>2020</b></div></div>
    <div class="meta"><i></i>0 Comments</div>
    <div class="ttl">Lorem Ipsum is simply dummy text of the printing and typesetting industry...</div>
    <div class="btn"><span class="dot" style="border-color:var(--deep);border-right-color:transparent;width:10px;height:10px"></span>Read More</div>
  </div>
  <div class="bcard" style="left:480px">
    <div class="img" role="img" aria-label="Woman exercising in a gym with a resistance band" style="background:linear-gradient(160deg,#7b5a78,#c26a86 50%,#3f3446)"><div class="date">10/09<b>2020</b></div></div>
    <div class="meta"><i></i>0 Comments</div>
    <div class="ttl">Lorem Ipsum is simply dummy text of the printing and typesetting industry...</div>
    <div class="btn"><span class="dot" style="border-color:var(--deep);border-right-color:transparent;width:10px;height:10px"></span>Read More</div>
  </div>
  <div class="bcard" style="left:739px">
    <div class="img" role="img" aria-label="Therapist treating a patient's shoulder in a clinic" style="background:linear-gradient(160deg,#d9dee0,#aab4b8 55%,#7a8488)"><div class="date">05/09<b>2020</b></div></div>
    <div class="meta"><i></i>0 Comments</div>
    <div class="ttl">Lorem Ipsum is simply dummy text of the printing and typesetting industry...</div>
    <div class="btn"><span class="dot" style="border-color:var(--deep);border-right-color:transparent;width:10px;height:10px"></span>Read More</div>
  </div>
</section>

<!-- Footer -->
<footer class="section footer">
  <div class="brand" style="left:181px;top:40px"><span class="mark"></span>The Willowmere Practice</div>
  <p class="tag">Restore your Energy for exceptional health and longevity</p>
  <h6 style="left:467px;top:28px">Quick links</h6>
  <div class="links" style="left:467px;top:60px">Home<br>Video<br>Why Energy<br>Our Process<br>About Bram</div>
  <div class="links" style="left:611px;top:60px">Our Services<br>Contact<br>Testimonials<br>Blogs</div>
  <h6 style="left:823px;top:28px">Contact Info</h6>
  <div class="contact">
    <div><svg width="14" height="11" viewBox="0 0 14 11"><rect x=".5" y=".5" width="13" height="10" fill="none" stroke="#5cc2cc"/><path d="M.5 .5l6.5 5 6.5-5" fill="none" stroke="#5cc2cc"/></svg>info@willowmere.example</div>
    <div><svg width="14" height="14" viewBox="0 0 24 24"><path d="M6.6 10.8a15 15 0 006.6 6.6l2.2-2.2a1 1 0 011-.25 11.4 11.4 0 003.6.6 1 1 0 011 1V20a1 1 0 01-1 1A17 17 0 013 4a1 1 0 011-1h3.5a1 1 0 011 1 11.4 11.4 0 00.6 3.6 1 1 0 01-.25 1z" fill="none" stroke="#5cc2cc" stroke-width="1.6"/></svg>+61 400 000 123</div>
    <div><svg width="14" height="16" viewBox="0 0 14 16"><path d="M7 15s-6-6-6-9a6 6 0 0112 0c0 3-6 9-6 9z" fill="none" stroke="#5cc2cc"/><circle cx="7" cy="6" r="2" fill="none" stroke="#5cc2cc"/></svg><span>Level 4, 12 Harbour Lane,<br>Sydney, Australia</span></div>
  </div>
</footer>
<div class="copybar">
  <span>Copyright © 2020 The Willowmere Practice. All Rights Reserved</span>
  <div class="social"><i></i><i></i><i style="background:#3a8f9b"></i><i></i></div>
</div>
</body>
</html>
```